Keystone Haulers Billboard design

I need two billboard designs using our logo and adding a few words Looking for a black background with our logo and wording in either purple or white.

need it to have our website keystonehaulers-example.com. phone number 555 201 4387

Also have 16/20/30 yard dumpsters available!

one billboard is size 7x21 feet the other is 15x 21 ft

Target Market(s)

Contractors, home owners

Requirements
Must have
• Use font similar to logo that is eye catching

```html
<!DOCTYPE html>
<html lang="en">
<head>
<meta charset="utf-8">
<title>Keystone Haulers Billboards</title>
<link href="https://fonts.googleapis.com/css2?family=Montserrat:wght@500;600;700;800&display=swap" rel="stylesheet">
<style>
  :root {
    --stage: #6b6c70;
    --board-black: #0d0d0d;
    --board-grey: #222222;
    --purple: #7e3f98;
    --white: #ffffff;
    --steel-blue: #2f5590;
    --steel-dark: #1c3561;
  }
  * { margin: 0; padding: 0; box-sizing: border-box; }
  html, body {
    width: 1053px; height: 1200px; overflow: hidden;
    background: var(--stage);
    font-family: "Montserrat", sans-serif;
  }
  .billboard {
    position: absolute; left: 127px; width: 800px;
    background: var(--white);
    box-shadow: 0 10px 22px rgba(0,0,0,0.45);
    overflow: hidden;
  }
  .billboard--wide { top: 136px; height: 266px; }
  .billboard--tall { top: 492px; height: 571px; }

  .billboard__field {
    position: absolute; left: 0; top: 0; width: 100%;
    background: radial-gradient(ellipse at 40% 40%, var(--board-grey), var(--board-black) 75%);
  }
  .billboard--wide .billboard__field { height: 217px; }
  .billboard--tall .billboard__field { height: 453px; }

  .brand-name {
    position: absolute; left: 32px; top: 22px; width: 430px;
    color: var(--white); font-weight: 800;
    font-size: 58px; line-height: 62px; text-transform: uppercase;
    letter-spacing: 1px; white-space: nowrap;
  }

  .contact-bar {
    position: absolute; left: -3px;
    border: 3px solid var(--purple);
    display: flex; align-items: center;
    color: var(--white); font-weight: 500;
    white-space: nowrap;
  }
  .billboard--wide .contact-bar { top: 174px; width: 465px; height: 32px; font-size: 16px; padding-left: 30px; gap: 16px; }
  .billboard--tall .contact-bar { top: 382px; width: 780px; height: 52px; font-size: 26px; padding-left: 34px; justify-content: space-between; padding-right: 16px; }
  .contact-bar__item { display: flex; align-items: center; gap: 7px; white-space: nowrap; }
  .contact-bar__icon { fill: var(--purple); flex: none; }

  .size-banner { position: absolute; left: 489px; top: -4px; }
  .size-banner__text {
    position: absolute; left: 0; top: 0; width: 289px;
    text-align: center; color: var(--white); font-weight: 600;
    white-space: nowrap;
  }
  .billboard--wide .size-banner__text { padding-top: 22px; }
  .billboard--wide .line-a { font-size: 28px; line-height: 32px; }
  .billboard--wide .line-b { font-size: 32px; line-height: 34px; font-weight: 800; }
  .billboard--wide .line-c { font-size: 21px; line-height: 26px; }
  .billboard--tall .size-banner__text { padding-top: 44px; }
  .billboard--tall .line-a { font-size: 42px; line-height: 50px; }
  .billboard--tall .line-b { font-size: 46px; line-height: 50px; font-weight: 800; }
  .billboard--tall .line-c { font-size: 46px; line-height: 48px; }

  .dumpster-photo {
    position: absolute;
    background: linear-gradient(180deg, var(--steel-blue), var(--steel-dark));
    border-radius: 3px;
  }
  .billboard--wide .dumpster-photo { left: 548px; top: 114px; width: 173px; height: 88px; }
  .billboard--tall .dumpster-photo { left: 67px; top: 180px; width: 361px; height: 179px; }

  .tagline {
    position: absolute; left: 0; width: 100%;
    text-align: center; color: var(--purple); font-weight: 800;
    white-space: nowrap;
  }
  .billboard--wide .tagline { top: 217px; height: 49px; line-height: 49px; font-size: 31px; }
  .billboard--tall .tagline { top: 453px; height: 118px; padding-top: 9px; font-size: 52px; line-height: 50px; }
</style>
</head>
<body>

<section class="billboard billboard--wide">
  <div class="billboard__field"></div>
  <div class="brand-name">Keystone<br>Haulers</div>
  <svg class="size-banner" width="289" height="140" viewBox="0 0 289 140">
    <polygon points="0,0 289,0 289,115 144.5,137 0,115" fill="var(--white)"/>
    <polygon points="5,0 284,0 284,111 144.5,132 5,111" fill="var(--purple)"/>
  </svg>
  <div class="size-banner" style="top:0">
    <div class="size-banner__text">
      <div class="line-a">Also Have</div>
      <div class="line-b">16 / 20 / 30 <span style="font-weight:600">Yard</span></div>
      <div class="line-c">Dumpsters Available!</div>
    </div>
  </div>
  <div class="dumpster-photo" role="img" aria-label="Photo of a blue roll-off dumpster"></div>
  <div class="contact-bar">
    <span class="contact-bar__item">
      <svg class="contact-bar__icon" width="13" height="13" viewBox="0 0 24 24"><path d="M6.6 10.8a15.2 15.2 0 0 0 6.6 6.6l2.2-2.2c.3-.3.7-.4 1-.2 1.1.4 2.3.6 3.6.6.6 0 1 .4 1 1V20c0 .6-.4 1-1 1A17 17 0 0 1 3 4c0-.6.4-1 1-1h3.5c.6 0 1 .4 1 1 0 1.3.2 2.5.6 3.6.1.3 0 .7-.2 1z"/></svg>
      555 201 4387
    </span>
    <span class="contact-bar__item">
      <svg class="contact-bar__icon" width="13" height="13" viewBox="0 0 24 24"><circle cx="12" cy="12" r="10"/><path d="M2 12h20M12 2c3 3 3 17 0 20M12 2c-3 3-3 17 0 20" stroke="var(--board-black)" stroke-width="1.4" fill="none"/></svg>
      keystonehaulers-example.com
    </span>
  </div>
  <div class="tagline">Residential &amp; Commercial Dumpster Rentals</div>
</section>

<section class="billboard billboard--tall">
  <div class="billboard__field"></div>
  <div class="brand-name">Keystone<br>Haulers</div>
  <svg class="size-banner" width="289" height="368" viewBox="0 0 289 368">
    <polygon points="0,0 289,0 289,326 144.5,367 0,326" fill="var(--white)"/>
    <polygon points="5,0 284,0 284,322 144.5,361 5,322" fill="var(--purple)"/>
  </svg>
  <div class="size-banner" style="top:0">
    <div class="size-banner__text">
      <div class="line-a">Also Have</div>
      <div class="line-b">16 / 20 / 30</div>
      <div class="line-c">Yard</div>
      <div class="line-c">Dumpsters</div>
      <div class="line-c">Available!</div>
    </div>
  </div>
  <div class="dumpster-photo" role="img" aria-label="Photo of a blue roll-off dumpster"></div>
  <div class="contact-bar">
    <span class="contact-bar__item">
      <svg class="contact-bar__icon" width="20" height="20" viewBox="0 0 24 24"><path d="M6.6 10.8a15.2 15.2 0 0 0 6.6 6.6l2.2-2.2c.3-.3.7-.4 1-.2 1.1.4 2.3.6 3.6.6.6 0 1 .4 1 1V20c0 .6-.4 1-1 1A17 17 0 0 1 3 4c0-.6.4-1 1-1h3.5c.6 0 1 .4 1 1 0 1.3.2 2.5.6 3.6.1.3 0 .7-.2 1z"/></svg>
      555 201 4387
    </span>
    <span class="contact-bar__item">
      <svg class="contact-bar__icon" width="20" height="20" viewBox="0 0 24 24"><circle cx="12" cy="12" r="10"/><path d="M2 12h20M12 2c3 3 3 17 0 20M12 2c-3 3-3 17 0 20" stroke="var(--board-black)" stroke-width="1.4" fill="none"/></svg>
      keystonehaulers-example.com
    </span>
  </div>
  <div class="tagline">Residential &amp; Commercial<br>Dumpster Rentals</div>
</section>

</body>
</html>
```